Letterhead and matching envelope design for a dental office

We need a new stationary design, letterhead and envelope #10, for a dental office in Denver area. We are called Fernhollow Dental. We want a simple and minimalistic design but not a boring design. I wish to have one good point that makes it look professional. I have attached our logo. Feel free to use either one. I want the design for letterhead and envelope look like a "matching pair" but not look the same. The envelope doesn't have to be white and it will have an address window on bottom left.

Target Market(s)

everyone who visits dentist (adults)

Industry/Entity Type

Dental

Font styles to use
Other font styles liked:
• close to font on logo or something that matches well

Requirements
Must have
• professional
• simple, minimalistic
• unique point that stands out
Nice to have
• matching but not same design for letterhead and envelope
Should not have
• not look like all the other boring designs
• no flowery, distracting feats

```html
<!DOCTYPE html>
<html lang="en">
<head>
<meta charset="utf-8">
<title>Fernhollow Dental Letterhead</title>
<link rel="stylesheet" href="https://fonts.googleapis.com/css2?family=Open+Sans:wght@400;600&display=swap">
<style>
  :root {
    --backdrop: #e6e6e6;
    --paper: #ffffff;
    --brand-green: #3aac48;
    --soft-green: #e6f4e8;
    --ink: #3a3a3a;
  }
  * { box-sizing: border-box; margin: 0; padding: 0; }
  html, body {
    width: 1200px;
    height: 1200px;
    overflow: hidden;
    background: var(--backdrop);
    font-family: "Open Sans", Arial, sans-serif;
  }
  .letterhead {
    position: absolute;
    left: 222px;
    top: 56px;
    width: 756px;
    height: 1088px;
    background: var(--paper);
    box-shadow: 0 2px 10px rgba(0,0,0,0.08);
  }
  .brand {
    position: absolute;
    left: 56px;
    top: 150px;
    display: flex;
    align-items: center;
    gap: 10px;
  }
  .brand-dot {
    width: 12px;
    height: 12px;
    border-radius: 50%;
    background: var(--brand-green);
  }
  .brand-name {
    font-size: 20px;
    font-weight: 600;
    letter-spacing: 2px;
    text-transform: uppercase;
    color: var(--brand-green);
  }
  .address {
    position: absolute;
    right: 80px;
    top: 70px;
    font-style: normal;
    font-size: 12px;
    line-height: 1.35;
    color: var(--ink);
  }
  .address-title {
    color: var(--brand-green);
    text-transform: uppercase;
  }
  .accent {
    position: absolute;
    right: 20px;
    top: 560px;
    width: 240px;
    height: 300px;
    border-radius: 50% 50% 40% 60%;
    background: radial-gradient(ellipse at 60% 40%, var(--soft-green), rgba(230,244,232,0) 70%);
  }
  .contact {
    position: absolute;
    left: 56px;
    bottom: 60px;
    list-style: none;
    font-size: 14px;
    line-height: 1.5;
    color: var(--ink);
  }
  .contact li { display: flex; align-items: center; gap: 8px; }
  .contact svg { width: 12px; height: 12px; fill: var(--brand-green); }
</style>
</head>
<body>
  <main class="letterhead">
    <div class="brand">
      <span class="brand-dot"></span>
      <span class="brand-name">Fernhollow Dental</span>
    </div>

    <address class="address">
      <div class="address-title">Fernhollow Dental</div>
      <div>2210 Alder Ridge Blvd Suite 40</div>
      <div>Lakewood, CO 80226</div>
    </address>

    <div class="accent" role="img" aria-label="Faint pale green leaf motif with soft sweeping lines"></div>

    <ul class="contact">
      <li>
        <svg viewBox="0 0 24 24"><path d="M6.6 10.8a15.1 15.1 0 0 0 6.6 6.6l2.2-2.2a1 1 0 0 1 1-.25 11.4 11.4 0 0 0 3.6.57 1 1 0 0 1 1 1V20a1 1 0 0 1-1 1A17 17 0 0 1 3 4a1 1 0 0 1 1-1h3.5a1 1 0 0 1 1 1c0 1.250.2 2.45.57 3.57a1 1 0 0 1-.25 1z"/></svg>
        720-555-0148
      </li>
      <li>
        <svg viewBox="0 0 24 24"><path d="M2 5h20v14H2z M2 5l10 8 10-8" stroke="#fff" stroke-width="1.5"/></svg>
        info@fernhollowdental.com
      </li>
      <li>
        <svg viewBox="0 0 24 24"><circle cx="12" cy="12" r="10"/><path d="M2 12h20M12 2c3 3 3 17 0 20M12 2c-3 3-3 17 0 20" stroke="#fff" stroke-width="1.5" fill="none"/></svg>
        www.fernhollowdental.com
      </li>
    </ul>
  </main>
</body>
</html>
```